Angebotsflyer - nicht Einladung -  für Personalmarketing Agentur
Angebotsflyer - nicht Einladung - für Personalmarketing Agentur
Zielgruppe
Wir sind eine Personalmarketing Agentur, die Unternehmen zu einer starken Arbeitgebermarke verhilft. Achtung: Wir sind keine Personalvermittler. Unternehmen, die als Arbeitgeber sichtbar werden möchten oder die ihre Mitarbeiterzufriedenheit steigern möchten sind unsere Zielgruppe.
Aufgabenstellung
DIN Lang. Wir möchten den Kreativen so viel Gestaltungsraum wie möglich lassen mit der Bitte sich nach unserer Website zu orientieren: www.teamfunke.works
Unser Leistungs-Portfolio sollte ansprechend dargestellt werden:
- Individuelles Recruiting
- Stellenanzeigen
- Mitarbeiterbefragungen
- Was Bewerber wollen
- Karriereseiten
- Mitarbeiter Benefits
- HR digital
- Corporate Fashion
- nUb Akademie (HR Workshops: Personalmarketing, Mitarbeitermotivation und -bindung, Stellenanzeigen, etc.)
nUb steht für never upset balance und für ehrliches Personalmarketing. Dabei ist es essentiell sich zunächst dem internen Personalmarketing zu widmen. Von innen heraus entsteht dann ein stimmiges externes Personalmarketingkonzept, welches von den Mitarbeitern getragen wird.
Gutes Personalmarketing ist mehr als das jährliche Grillfest.

```html
<!DOCTYPE html>
<html lang="de">
<head>
<meta charset="utf-8">
<title>nUb Personalmarketing – DIN-lang-Flyer</title>
<link rel="stylesheet" href="https://fonts.googleapis.com/css2?family=Open+Sans:wght@400;600;700;800&display=swap">
<style>
:root{
  --backdrop:#dadada;
  --navy:#133d58;
  --navy-deep:#0c3450;
  --blue:#0068a0;
  --teal:#1b9bb0;
  --gold:#a68a5b;
  --icon:#6e7e91;
  --ink:#1b3a55;
  --text:#3d4b58;
  --white:#ffffff;
}
*{box-sizing:border-box;margin:0;padding:0}
html,body{width:1154px;height:1200px;overflow:hidden}
body{background:var(--backdrop);font-family:"Open Sans",Arial,sans-serif;position:relative;color:var(--ink)}
.sheet{position:absolute;height:535px;box-shadow:4px 5px 10px rgba(0,0,0,.25);overflow:hidden;background:var(--white)}
.cover{left:55px;top:51px;width:252px}
.spread-outer{left:340px;top:50px;width:757px}
.spread-inner{left:340px;top:612px;width:757px}
.panel{position:absolute;top:0;width:252px;height:535px;overflow:hidden}
.panel.p1{left:0}.panel.p2{left:252px}.panel.p3{left:504px}
.fold{position:absolute;top:0;width:1px;height:100%;background:rgba(0,0,0,.12);z-index:5}
.layer{position:absolute;inset:0}
.caption{position:absolute;left:56px;top:597px;font-size:12.5px;color:#222}

/* title panel */
.brand-head{position:absolute;left:0;top:0;width:252px;height:158px;background:var(--navy);display:flex;flex-direction:column;align-items:center;justify-content:center;gap:4px}
.brand-name{font-weight:700;font-size:56px;color:var(--white);line-height:1}
.brand-line{font-size:8px;letter-spacing:1.6px;color:var(--white);text-transform:uppercase}
.visual{position:absolute;left:0;top:158px;width:252px;height:377px;background:radial-gradient(ellipse 55% 45% at 50% 50%,#2e6f88 0%,#173a52 55%,#0f2234 100%)}

/* intro panel */
.intro{background:var(--navy)}
.marker{position:absolute;left:0}
.intro-title{position:absolute;left:39px;top:36px;font-size:21px;font-weight:600;color:var(--white)}
.intro-text{position:absolute;left:39px;top:75px;width:186px;font-size:11.3px;line-height:14.4px;color:var(--white)}
.intro-text p+p{margin-top:14px}
.bulbs{position:absolute;left:0;top:270px;width:252px;height:243px;background:radial-gradient(circle at 30% 55%,#e08a2a 0%,#6b3410 22%,#1e1209 50%,#120c08 100%)}

/* contact panel */
.contact{position:absolute;left:24px;top:178px;width:215px;color:var(--ink)}
.contact h2{font-size:10.2px;font-weight:600;line-height:14.5px}
.contact p{font-size:9.2px;line-height:12px;color:var(--text)}
.contact .addr{margin-top:12px}
.contact dl{margin-top:10px;display:grid;grid-template-columns:40px 1fr;font-size:9.2px;line-height:12px;color:var(--text)}
.contact .cta{margin-top:22px;font-size:9.4px;font-weight:600;line-height:11.5px;color:var(--ink)}

/* inner spread */
.headline{position:absolute;left:39px;top:34px;font-size:22px;font-weight:700;color:var(--white);letter-spacing:.2px;z-index:3}
.subline{position:absolute;left:39px;top:74px;font-size:15px;font-weight:600;color:var(--white);z-index:3}
.section-title{position:absolute;left:38px;top:143px;font-size:14.5px;font-weight:700;color:var(--ink)}
.section-rule{position:absolute;left:38px;top:163px}
.web{position:absolute;left:39px;top:379px;font-size:11px;font-weight:600;color:var(--ink);transform:rotate(15.5deg);transform-origin:left top;z-index:3}
.service{position:absolute;width:200px;display:grid;grid-template-columns:64px 1fr;z-index:3}
.service svg{width:52px;height:44px}
.service h3{font-size:11.2px;font-weight:700;color:var(--ink);line-height:12px;text-transform:uppercase}
.service p{margin-top:6px;font-size:6.9px;line-height:9.8px;color:var(--text)}
.small-brand{position:absolute;left:504px;top:36px;width:252px;text-align:center;z-index:3}
.small-brand .brand-name{font-size:40px}
.small-brand .brand-line{font-size:6px;margin-top:4px}
</style>
</head>
<body>

<section class="sheet cover">
  <div class="brand-head">
    <div class="brand-name">nUb</div>
    <div class="brand-line">never upset balance</div>
  </div>
  <div class="visual" role="img" aria-label="Foto: Geschäftsmann im Anzug hält die offenen Hände, darüber schwebende Personen-Symbole als Netzwerk"></div>
  <svg class="layer" width="252" height="535" viewBox="0 0 252 535">
    <defs>
      <linearGradient id="coverTeal" x1="0" x2="1"><stop offset="0" stop-color="#1a9ab0"/><stop offset="1" stop-color="#3fb2c2"/></linearGradient>
    </defs>
    <polygon points="0,468 252,535 0,535" fill="url(#coverTeal)"/>
    <polygon points="252,468 252,535 140,535" fill="#0b5c92"/>
    <line x1="0" y1="458" x2="252" y2="535" stroke="var(--gold)" stroke-width="1.4"/>
  </svg>
</section>
<div class="caption">Titel, gefaltet</div>

<section class="sheet spread-outer">
  <div class="panel p1 intro">
    <svg class="marker" width="34" height="40" viewBox="0 0 34 40" style="top:29px"><polygon points="0,0 34,20 0,40" fill="var(--gold)"/></svg>
    <h1 class="intro-title">nUb</h1>
    <div class="intro-text">
      <p>nUb steht für never upset balance und für ehrliches Personal&shy;marketing. Dabei ist es essentiell sich zunächst dem internen Personalmarketing zu widmen. Von innen heraus entsteht dann ein stimmiges externes Personal&shy;marketingkonzept, welches von den Mitarbeitern getragen wird.</p>
      <p>Gutes Personalmarketing ist mehr als das jährliche Grillfest.</p>
    </div>
    <div class="bulbs" role="img" aria-label="Foto: zwei leuchtende Glühbirnen mit Glühfaden vor dunklem Hintergrund"></div>
  </div>

  <div class="panel p2">
    <svg class="layer" width="252" height="535" viewBox="0 0 252 535">
      <defs>
        <linearGradient id="backBlue" x1="0" y1="0" x2="1" y2="0.3"><stop offset="0" stop-color="#0a4c73"/><stop offset="1" stop-color="#0066a0"/></linearGradient>
        <linearGradient id="backFoot" x1="0" y1="0" x2="1" y2="0"><stop offset="0" stop-color="#0062a0"/><stop offset="1" stop-color="#138fb0"/></linearGradient>
      </defs>
      <rect width="252" height="535" fill="url(#backBlue)"/>
      <polygon points="0,86 252,166 252,535 0,535" fill="#fff"/>
      <polygon points="0,386 252,462 252,535 0,535" fill="url(#backFoot)"/>
      <line x1="0" y1="82" x2="252" y2="162" stroke="var(--gold)" stroke-width="1.6"/>
      <line x1="0" y1="381" x2="252" y2="458" stroke="var(--gold)" stroke-width="1.6"/>
    </svg>
    <div class="contact">
      <h2>nUb Personalmarketing GmbH<br>Wir schaffen ehrliches Personalmarketing</h2>
      <p class="addr">Mara Lindholm<br>Kastanienstraße 22<br>28211 Bremen</p>
      <dl>
        <dt>Telefon:</dt><dd>04 21 55 01 23 45</dd>
        <dt>E-Mail:</dt><dd>info@nub-jetzt.de</dd>
        <dt>Web:</dt><dd>www.teamfunke.works</dd>
      </dl>
      <p class="cta">Jetzt Termin für kostenloses Erstgespräch vereinbaren.</p>
    </div>
  </div>

  <div class="panel p3">
    <div class="brand-head">
      <div class="brand-name">nUb</div>
      <div class="brand-line">never upset balance</div>
    </div>
    <div class="visual" role="img" aria-label="Foto: Geschäftsmann im Anzug hält die offenen Hände, darüber schwebende Personen-Symbole als Netzwerk"></div>
    <svg class="layer" width="252" height="535" viewBox="0 0 252 535">
      <polygon points="0,468 252,535 0,535" fill="#2aa5b8"/>
      <polygon points="252,468 252,535 140,535" fill="#0b5c92"/>
      <line x1="0" y1="458" x2="252" y2="535" stroke="var(--gold)" stroke-width="1.4"/>
    </svg>
  </div>
  <div class="fold" style="left:252px"></div>
  <div class="fold" style="left:504px"></div>
</section>

<section class="sheet spread-inner">
  <svg class="layer" width="757" height="535" viewBox="0 0 757 535">
    <defs>
      <linearGradient id="headBlue" x1="0" y1="0" x2="1" y2="0"><stop offset="0" stop-color="#0b4a72"/><stop offset="1" stop-color="#0066a0"/></linearGradient>
      <linearGradient id="footBlue" x1="0" y1="0" x2="1" y2="0"><stop offset="0" stop-color="#0062a0"/><stop offset="1" stop-color="#139ab2"/></linearGradient>
    </defs>
    <rect x="0" y="0" width="504" height="128" fill="var(--navy)"/>
    <polygon points="170,0 504,0 504,128 440,128" fill="url(#headBlue)" opacity=".85"/>
    <polygon points="0,0 210,0 0,128" fill="var(--navy)"/>
    <polygon points="504,0 757,0 757,170 590,128 504,128" fill="var(--navy)"/>
    <line x1="585" y1="128" x2="757" y2="172" stroke="var(--gold)" stroke-width="1.8"/>
    <polygon points="0,405 496,535 0,535" fill="url(#footBlue)"/>
    <line x1="0" y1="399" x2="496" y2="535" stroke="var(--gold)" stroke-width="1.6"/>
    <polygon points="0,27 31,45 0,63" fill="var(--gold)"/>
  </svg>

  <h1 class="headline">EHRLICHES PERSONALMARKETING</h1>
  <p class="subline">Ihr Personalmarketing &amp; Employer Branding ist unsere Mission</p>

  <div class="small-brand">
    <div class="brand-name">nUb</div>
    <div class="brand-line">never upset balance</div>
  </div>

  <h2 class="section-title">UNSERE LEISTUNGEN</h2>
  <svg class="section-rule" width="150" height="10" viewBox="0 0 150 10"><polyline points="0,1.5 70,1.5 75,6.5 80,1.5 150,1.5" fill="none" stroke="var(--gold)" stroke-width="1.6"/></svg>

  <div class="web">www.teamfunke.works</div>

  <article class="service" style="left:38px;top:188px">
    <svg viewBox="0 0 52 44"><rect x="5" y="6" width="38" height="26" rx="2" fill="none" stroke="var(--icon)" stroke-width="3"/><path d="M0 36h48l-3 4H3z" fill="var(--icon)"/><path d="M44 4l3-4M47 8l4-1" stroke="var(--gold)" stroke-width="1.5"/></svg>
    <div><h3>HR Digital</h3><p>Karriereseite, Social Media Recruiting, Bewerbermanagementsystem, digitale Dienstpläne, Online-Storytelling, Talent­pools oder Jobportale – es führt kein Weg mehr daran vorbei.</p></div>
  </article>
  <article class="service" style="left:38px;top:278px">
    <svg viewBox="0 0 52 44"><circle cx="24" cy="24" r="10" fill="var(--icon)"/><rect x="19" y="34" width="10" height="8" rx="1.5" fill="var(--icon)"/><path d="M24 2v6M10 8l4 4M38 8l-4 4M4 18l6 2M44 18l-6 2" stroke="var(--gold)" stroke-width="2"/></svg>
    <div><h3>Das TASI Prinzip</h3><p>Die Abkürzung TASI steht für TeamAnalyseStatusIndex. Mithilfe des TASI-Prinzips können wir die IST-Situation Ihres Unternehmens erfassen. Diese Analyse ist entscheidend.</p></div>
  </article>

  <article class="service" style="left:278px;top:188px;width:210px">
    <svg viewBox="0 0 52 44"><circle cx="30" cy="16" r="11" fill="none" stroke="var(--icon)" stroke-width="3.5"/><path d="M38 25l10 10" stroke="var(--icon)" stroke-width="5" stroke-linecap="round"/><rect x="2" y="27" width="24" height="9" rx="4" fill="var(--gold)"/></svg>
    <div><h3>Individuelles<br>Recruiting</h3><p>Recruiting sollte so individuell sein, wie Ihr Unternehmen. Um für Sie den idealen Weg zu finden, bedienen wir uns an den aktuellen Trends und Möglichkeiten.</p></div>
  </article>
  <article class="service" style="left:278px;top:278px;width:210px">
    <svg viewBox="0 0 52 44"><rect x="3" y="2" width="44" height="40" rx="2" fill="none" stroke="var(--icon)" stroke-width="3"/><rect x="3" y="2" width="44" height="6" fill="var(--icon)"/><text x="25" y="36" text-anchor="middle" font-family="Open Sans,Arial,sans-serif" font-size="28" font-weight="700" fill="var(--icon)">@</text></svg>
    <div><h3>Karriereseite &amp; Co</h3><p>Wir machen Sie im Internet sichtbar. 75% aller Bewerber verschaffen sich ihren ersten Eindruck über die Internetseite des potentiellen Arbeitgebers.</p></div>
  </article>
  <article class="service" style="left:278px;top:367px;width:210px">
    <svg viewBox="0 0 52 44"><circle cx="38" cy="9" r="7" fill="var(--icon)"/><path d="M33 14L10 34" stroke="var(--icon)" stroke-width="5" stroke-linecap="round"/><path d="M32 12l4 4" stroke="var(--gold)" stroke-width="2"/><path d="M9 35c-4 3-3 7 0 8" fill="none" stroke="var(--gold)" stroke-width="1.5"/></svg>
    <div><h3>Mitarbeiterbefragung</h3><p>Eine Mitarbeiterbefragung ist meist der ideale Einstieg zum Aufbau einer Arbeit­gebermarke. Planen Sie mit uns Ihre Mitarbeiterbefragung individuell &amp; profes­sionell, zu einem realistischen Preis.</p></div>
  </article>

  <article class="service" style="left:529px;top:188px">
    <svg viewBox="0 0 52 44"><path d="M14 2h8a4 4 0 008 0h8l12 8-5 9-6-3v28H14V16l-6 3-5-9z" fill="var(--icon)"/><circle cx="34" cy="16" r="3" fill="none" stroke="#fff" stroke-width="1.2"/></svg>
    <div><h3>Corporate Fashion</h3><p>Auch das Thema Berufsbekleidung ist ein sehr bedeutender Faktor für die Zufriedenheit am Arbeitsplatz. Gern unterstützen wir Sie bei der Auswahl geeigneter Modelle und Lieferanten.</p></div>
  </article>
  <article class="service" style="left:529px;top:278px">
    <svg viewBox="0 0 52 44"><path d="M6 2h30v36l-6 6H6z" fill="none" stroke="var(--icon)" stroke-width="3"/><path d="M11 10h20M11 16h20M11 22h14" stroke="var(--icon)" stroke-width="2"/><path d="M46 4L22 32l-2 6 6-2L50 8z" fill="var(--icon)"/></svg>
    <div><h3>Stellenanzeigen</h3><p>Eine gut und kreativ formulierte Anzeige, die sich von anderen abhebt und dann auch noch sinnig platziert wird, kann bei der Suche nach neuen Mitarbeitern wahre Wunder bewirken.</p></div>
  </article>
  <article class="service" style="left:529px;top:367px">
    <svg viewBox="0 0 52 44"><circle cx="12" cy="10" r="9" fill="var(--gold)"/><path d="M12 5v10M7 10h10" stroke="#fff" stroke-width="2"/><path d="M2 30c6-6 14-6 20-2h12c4 0 4 5 0 5H22l14 1 10-6c4-2 6 2 3 4L34 42H14L2 36z" fill="var(--icon)"/></svg>
    <div><h3>Mitarbeiterbenefits</h3><p>Unser Leitspruch: „Modernes Mitarbei­termarketing ist mehr als ein jährliches Grillfest“. Sind Ihre Mitarbeiter zufrie­den, werden sie automatisch zu Ihren Markenbotschaftern.</p></div>
  </article>
  <article class="service" style="left:529px;top:456px">
    <svg viewBox="0 0 52 44"><path d="M6 4h44v28H26" fill="none" stroke="var(--gold)" stroke-width="2.5"/><circle cx="12" cy="26" r="5" fill="var(--icon)"/><circle cx="24" cy="24" r="5" fill="var(--icon)"/><circle cx="35" cy="26" r="5" fill="var(--icon)"/><path d="M2 40c0-7 20-9 22-9s20 2 20 9z" fill="var(--icon)"/></svg>
    <div><h3>nUb Akademie</h3><p>HR Workshops: Personalmarketing, Mitarbeitermotivation und -bindung, Stellenanzeigen, etc.</p></div>
  </article>

  <div class="fold" style="left:252px"></div>
  <div class="fold" style="left:504px"></div>
</section>

</body>
</html>
```